Fence Flyer to Attract More Sales During Winter

We need a new flyer made that we can distribute to residential mailboxes. The flyer is to promote our Frostline Picket Days. We like simply designs, and we would like the flyer to showcase a lot of our fence photos. More of our photos are online at our website at www.getbramblerail.com - our new address needs to also be featured on the flyer - 436 Quillen rd, Monroe, NC 28117. I do want the words "FROSTLINE PICKET DAYS" to be dominate on the flyer with the description "Wood fences starting at $12/FT!" Please look through our Facebook page and our website to gather more photos or information. We are flexible on colors, nothing to fancy - simple flyer design please.

Target Market(s)

Residential homeowners that need a new fence to enclose their yard for safety, security or decorative

Industry/Entity Type

Residential Construction

Font styles to use
Sans Serif

Colors

Designer to choose colors to be used in the design.

Requirements
Must have
• Frostline Picket Days
• Contact information for the business
• "Come visit our outdoor showroom, open 24/7!"
Nice to have
• Photos of our fences - you can find more on our website at www.GetBrambleRail.com or Facebook.com/MeadowlarkRailGPV
Should not have
• Flashy designs

```html
<!DOCTYPE html>
<html lang="en">
<head>
<meta charset="utf-8">
<title>Frostline Picket Days – Bramblerail Fence</title>
<link rel="stylesheet" href="https://fonts.googleapis.com/css2?family=Alfa+Slab+One&family=Oswald:wght@600&family=Roboto:wght@400;500;700&family=Roboto+Slab:wght@400;500&display=swap">
<style>
  :root {
    --sky-top: #2f5f9c;
    --sky-low: #9fb6cc;
    --fence-light: #e8dcb4;
    --fence-mid: #cdbb8a;
    --lawn: #6f8a44;
    --navy: #1d3f72;
    --blue: #3477c2;
    --paper: #f4f4f6;
    --grey: #d9dadf;
    --tan: #c9b68a;
    --tan-light: #f1e6cf;
    --ink: #1e1e24;
    --white: #ffffff;
    --brand-blue: #2d78bf;
    --brand-brown: #6b3f22;
    --brand-orange: #e98b2a;
  }
  html, body { margin: 0; padding: 0; overflow: hidden; background: #e6e6e6; }
  .flyer {
    position: relative;
    width: 1200px;
    height: 928px;
    overflow: hidden;
    font-family: "Roboto", Arial, sans-serif;
    color: var(--ink);
  }
  .hero-photo {
    position: absolute; inset: 0 0 auto 0; height: 560px;
    background: linear-gradient(180deg, var(--sky-top) 0%, var(--sky-low) 22%, #8a6f5a 26%, var(--fence-light) 34%, var(--fence-mid) 62%, var(--lawn) 100%);
  }
  .panels { position: absolute; inset: 0; }
  .logo-card {
    position: absolute; left: 772px; top: 26px; width: 470px; height: 104px;
    background: var(--white);
    border: 5px solid var(--brand-brown);
    border-right: none;
    border-radius: 54px 0 0 54px;
    box-shadow: 0 0 0 5px var(--tan-light), 0 4px 10px rgba(0,0,0,.3);
    box-sizing: border-box;
    display: flex; align-items: center; padding-left: 34px; gap: 18px;
  }
  .logo-mark { width: 40px; height: 40px; background: var(--brand-orange); flex: none; }
  .logo-name { font: 700 34px/1 "Roboto", Arial, sans-serif; color: var(--brand-blue); margin: 0; }
  .logo-tagline { font: 700 12.5px/1.4 "Roboto", Arial, sans-serif; color: var(--ink); margin: 6px 0 0; }
  .headline {
    position: absolute; left: 38px; top: 76px; margin: 0;
    font-family: "Alfa Slab One", Georgia, serif; font-weight: 400;
    color: var(--white); text-transform: uppercase;
    text-shadow: 0 3px 8px rgba(0,0,0,.35);
  }
  .headline span { display: block; }
  .headline .line-1 { font-size: 76px; line-height: 1; }
  .headline .line-2 { font-size: 96px; line-height: 1.02; }
  .headline .line-3 { font: 700 58px/1.15 "Roboto", Arial, sans-serif; letter-spacing: 58px; }
  .offer {
    position: absolute; left: 40px; top: 322px; margin: 0;
    color: var(--white); text-shadow: 0 2px 6px rgba(0,0,0,.45);
  }
  .offer-price { display: block; font: 700 28px/1.2 "Roboto", Arial, sans-serif; }
  .offer-showroom { display: block; font: 500 19px/1.3 "Roboto", Arial, sans-serif; margin-top: 4px; }
  .photo {
    position: absolute; margin: 0; background: var(--white); padding: 12px 12px 44px;
    box-shadow: 0 6px 16px rgba(0,0,0,.35);
  }
  .photo .shot { width: 100%; height: 100%; }
  .photo-gate { left: 74px; top: 402px; width: 292px; height: 220px; }
  .photo-gate .shot { background: linear-gradient(180deg, #7fa5d8 0%, #c8b89a 35%, #b49c72 100%); }
  .photo-side { left: 300px; top: 450px; width: 256px; height: 238px; transform: rotate(-3deg); }
  .photo-side .shot { background: linear-gradient(180deg, #c9c9cc 0%, #d8c69c 30%, #b59d6e 100%); }
  .photo-garden { left: 552px; top: 446px; width: 300px; height: 232px; transform: rotate(-4deg); }
  .photo-garden .shot { background: linear-gradient(180deg, #7b9a5d 0%, #b79a6a 45%, #5e7d3a 100%); }
  .photo-yard { left: 806px; top: 388px; width: 292px; height: 216px; transform: rotate(-4deg); }
  .photo-yard .shot { background: linear-gradient(180deg, #5f7e4b 0%, #d7c79e 45%, #6d9a43 100%); }
  .contact-left { position: absolute; left: 0; width: 400px; text-align: center; color: var(--white); font-size: 18px; line-height: 1.3; }
  .contact-address { top: 700px; }
  .contact-email { top: 812px; }
  .contact-left .icon { display: block; margin: 0 auto 8px; }
  .contact-left p { margin: 0; }
  .estimate { position: absolute; left: 418px; width: 400px; top: 760px; text-align: center; }
  .estimate-label { font: 500 19px/1 "Roboto", Arial, sans-serif; margin: 0; }
  .estimate-phone { font: 600 58px/1 "Oswald", "Arial Narrow", sans-serif; color: var(--ink); margin: 16px 0 0; letter-spacing: 1px; }
  .estimate-web { font: 500 18px/1 "Roboto", Arial, sans-serif; letter-spacing: 2px; margin: 20px 0 0; }
  .services { position: absolute; left: 920px; top: 704px; }
  .services h2 { font: 400 42px/1 "Alfa Slab One", Georgia, serif; margin: 0 0 26px; }
  .services ul { list-style: none; margin: 0; padding: 0; }
  .services li { font: 400 23px/1 "Roboto Slab", Georgia, serif; display: flex; align-items: center; gap: 8px; margin-bottom: 13px; }
</style>
</head>
<body>
<main class="flyer">
  <div class="hero-photo" role="img" aria-label="Photo of a new wooden shadowbox privacy fence in front of a brick house under a blue winter sky"></div>

  <svg class="panels" width="1200" height="928" viewBox="0 0 1200 928" aria-hidden="true">
    <defs>
      <linearGradient id="centerGrad" x1="0" y1="0" x2="0" y2="1">
        <stop offset="0" stop-color="#d9dadf"/>
        <stop offset="1" stop-color="#f4f4f6"/>
      </linearGradient>
      <radialGradient id="blueGrad" cx=".55" cy=".55" r=".8">
        <stop offset="0" stop-color="#3477c2"/>
        <stop offset="1" stop-color="#1d3f72"/>
      </radialGradient>
      <radialGradient id="tanGrad" cx=".6" cy=".7" r=".8">
        <stop offset="0" stop-color="#f1e6cf"/>
        <stop offset="1" stop-color="#c9b68a"/>
      </radialGradient>
    </defs>
    <path d="M0,520 Q600,440 1200,520 L1200,928 L0,928 Z" fill="url(#centerGrad)"/>
    <path d="M0,350 Q300,370 392,560 Q440,640 420,928 L0,928 Z" fill="url(#blueGrad)"/>
    <path d="M1200,340 Q950,380 870,610 Q830,760 840,928 L1200,928 Z" fill="url(#tanGrad)"/>
  </svg>

  <header class="logo-card">
    <span class="logo-mark"></span>
    <div>
      <p class="logo-name">Bramblerail Fence</p>
      <p class="logo-tagline">"Because Good Fences Make Good Neighbors"</p>
    </div>
  </header>

  <h1 class="headline">
    <span class="line-1">Frostline</span>
    <span class="line-2">Picket</span>
    <span class="line-3">Days</span>
  </h1>

  <p class="offer">
    <span class="offer-price">Wood fences starting at $12/FT!</span>
    <span class="offer-showroom">Come visit our outdoor showroom, open 24/7!</span>
  </p>

  <figure class="photo photo-gate"><div class="shot" role="img" aria-label="Photo of an arched wooden gate with black hinges"></div></figure>
  <figure class="photo photo-side"><div class="shot" role="img" aria-label="Photo of a wooden picket fence beside a house with a company sign"></div></figure>
  <figure class="photo photo-garden"><div class="shot" role="img" aria-label="Photo of a wooden privacy fence along a garden bed with red roses"></div></figure>
  <figure class="photo photo-yard"><div class="shot" role="img" aria-label="Photo of a long wooden shadowbox fence around a green lawn"></div></figure>

  <div class="contact-left contact-address">
    <svg class="icon" width="32" height="42" viewBox="0 0 32 42"><path d="M16 1C8 1 2 7 2 15c0 10 14 26 14 26s14-16 14-26C30 7 24 1 16 1z" fill="#fff"/><circle cx="16" cy="15" r="6" fill="#3477c2"/></svg>
    <p>436 Quillen rd,</p>
    <p>Monroe, NC 28117</p>
  </div>
  <div class="contact-left contact-email">
    <svg class="icon" width="36" height="26" viewBox="0 0 36 26"><rect x="1" y="1" width="34" height="24" fill="#fff"/><path d="M2 2l16 13L34 2" fill="none" stroke="#3477c2" stroke-width="2.5"/></svg>
    <p>office@getbramblerail.com</p>
  </div>

  <section class="estimate">
    <p class="estimate-label">Get Free Estimate Today!</p>
    <p class="estimate-phone">704-555-0142</p>
    <p class="estimate-web">www.getbramblerail.com</p>
  </section>

  <section class="services">
    <h2>We Offer:</h2>
    <ul>
      <li><svg width="24" height="24" viewBox="0 0 24 24"><circle cx="12" cy="12" r="11" fill="#1e1e24"/><path d="M7 7v11M10 7v11M14 7v11M17 7v11M5 10h14M5 15h14" stroke="#fff" stroke-width="1.6"/></svg>Wood Fence</li>
      <li><svg width="24" height="24" viewBox="0 0 24 24"><circle cx="12" cy="12" r="11" fill="#1e1e24"/><path d="M7 8v10M10 8v10M14 8v10M17 8v10M5 11h14M5 16h14" stroke="#fff" stroke-width="1.4"/></svg>Aluminum Fences</li>
      <li><svg width="24" height="24" viewBox="0 0 24 24"><circle cx="12" cy="12" r="11" fill="#1e1e24"/><rect x="6" y="9" width="12" height="8" fill="#fff"/><path d="M5 8h14" stroke="#fff" stroke-width="2"/></svg>Trash Enclosure</li>
    </ul>
  </section>
</main>
</body>
</html>
```